Henri Marsac - Magician and Mentalist

I am a professional magician - mentalist based in Belgium. My stage name is Henri Marsac. I need a flyer (that I could use electronically or in print) to promote my activity. The flyer should represent myself "hand drawn" together with some classical attributes of a magician / mentalist : playing cards, billets, a crystal ball, some items related to mystery and conjuring... My logo has already been designed and I attach it enclosed. I also enclose a few pictures of me and a previous drawing that was made by a friend, but I am not satisfied with. As an example of what I like, I very much like the graphics of the poster of "Hollow Signals" (also enclosed). But it can be something totally different. See also my website for some graphic "feeling" : www.henrimarsac-demo.be

Target Market(s)

General public

Industry/Entity Type

Magician

Font styles to use
Other font styles liked:
• Old Newspaper Types (font enclosed in the uploaded files)

Colors

Designer to choose colors to be used in the design.

Requirements
Must have
• The project should reflect mystery/conjuring, and some items related to it (mainly playing cards but other elements may be inserted : a dice, ESP symbols, a "?" sign. Please see the enclosed files also.
Should not have
• I am not a "traditional" magician, so classic magic-related items like a hat, or a rabbit, or silks... should not appear in the design please.

```html
<!DOCTYPE html>
<html lang="fr">
<head>
<meta charset="utf-8">
<title>Henri Marsac – Mentaliste</title>
<link href="https://fonts.googleapis.com/css2?family=Old+Standard+TT:wght@400;700&display=swap" rel="stylesheet">
<style>
  :root {
    --bg-deep: #070303;
    --bg-red: #5a0c06;
    --bg-ember: #8e1d0c;
    --gold: #f3b53a;
    --star: #f6c23a;
    --cream: #f6efe2;
    --white: #ffffff;
    --photo-dark: #1b1a1e;
    --photo-mid: #3b3437;
  }
  * { margin: 0; padding: 0; box-sizing: border-box; }
  html, body { width: 846px; height: 1200px; overflow: hidden; background: var(--bg-deep); }
  .flyer {
    position: relative; width: 846px; height: 1200px; overflow: hidden;
    font-family: "Old Standard TT", Georgia, serif;
    background:
      radial-gradient(ellipse 60% 45% at 38% 32%, var(--bg-ember) 0%, var(--bg-red) 35%, transparent 75%),
      radial-gradient(ellipse 80% 60% at 45% 55%, #3a0805 0%, transparent 80%),
      var(--bg-deep);
  }
  .brand {
    position: absolute; left: 232px; top: 130px; width: 140px;
    display: flex; align-items: center; gap: 8px;
    color: var(--cream); font-size: 17px; font-weight: 700;
  }
  .brand-dot { width: 12px; height: 12px; border-radius: 50%; background: var(--cream); flex: none; }
  .stars { position: absolute; left: 82px; display: flex; gap: 14px; }
  .stars svg { width: 19px; height: 19px; fill: var(--star); }
  .stars--top { top: 240px; }
  .stars--bottom { top: 433px; }
  .reviews { position: absolute; left: 84px; top: 272px; list-style: none; color: var(--cream); font-size: 18px; font-weight: 700; }
  .reviews li { height: 30px; line-height: 30px; }
  .portrait {
    position: absolute; left: 424px; top: 52px; width: 346px; height: 500px;
    border-radius: 46% 46% 12% 12% / 28% 28% 8% 8%;
    background: linear-gradient(180deg, var(--photo-mid) 0%, var(--photo-dark) 45%, #0d0b0d 100%);
  }
  .headline {
    position: absolute; left: 0; top: 502px; width: 846px; text-align: center;
    color: var(--gold); font-size: 31px; font-weight: 700;
  }
  .intro, .offer {
    position: absolute; left: 40px; width: 766px; text-align: center;
    font-size: 20.5px; line-height: 26.5px;
  }
  .intro { top: 556px; color: var(--gold); }
  .intro strong { color: var(--white); }
  .offer { top: 709px; color: var(--gold); }
  .formula { position: absolute; display: flex; align-items: flex-start; gap: 14px; color: var(--gold); font-size: 19.5px; line-height: 24px; }
  .formula svg { width: 28px; height: 30px; fill: var(--white); flex: none; margin-top: 6px; }
  .formula--reception { left: 76px; top: 824px; }
  .formula--stage { left: 76px; top: 888px; }
  .formula--corporate { left: 474px; top: 826px; }
  .formula--evening { left: 474px; top: 890px; }
  .contact-label { position: absolute; top: 977px; width: 846px; text-align: center; color: var(--gold); font-size: 19px; font-weight: 700; }
  .contact { position: absolute; top: 1013px; width: 846px; text-align: center; color: var(--white); font-size: 20.5px; font-weight: 700; }
  .credentials { position: absolute; top: 1063px; width: 846px; text-align: center; color: var(--gold); font-size: 14.5px; line-height: 20px; font-weight: 700; }
  .disclaimer { position: absolute; top: 1114px; width: 846px; text-align: center; color: var(--gold); font-size: 14.5px; font-weight: 700; }
</style>
</head>
<body>
<main class="flyer">
  <div class="brand"><span class="brand-dot"></span>Henri Marsac</div>

  <div class="stars stars--top">
    <svg viewBox="0 0 24 24"><path d="M12 1l3.4 7 7.6 1-5.5 5.3 1.3 7.6L12 18.3 5.2 21.9l1.3-7.6L1 9l7.6-1z"/></svg>
    <svg viewBox="0 0 24 24"><path d="M12 1l3.4 7 7.6 1-5.5 5.3 1.3 7.6L12 18.3 5.2 21.9l1.3-7.6L1 9l7.6-1z"/></svg>
    <svg viewBox="0 0 24 24"><path d="M12 1l3.4 7 7.6 1-5.5 5.3 1.3 7.6L12 18.3 5.2 21.9l1.3-7.6L1 9l7.6-1z"/></svg>
    <svg viewBox="0 0 24 24"><path d="M12 1l3.4 7 7.6 1-5.5 5.3 1.3 7.6L12 18.3 5.2 21.9l1.3-7.6L1 9l7.6-1z"/></svg>
    <svg viewBox="0 0 24 24"><path d="M12 1l3.4 7 7.6 1-5.5 5.3 1.3 7.6L12 18.3 5.2 21.9l1.3-7.6L1 9l7.6-1z"/></svg>
  </div>
  <ul class="reviews">
    <li>« Absolutely fantastic ! »</li>
    <li>« Vous avez ravi tous nos invités »</li>
    <li>« Tout simplement magistral »</li>
    <li>« Epoustouflant ! »</li>
    <li>« Quelle fabuleuse expérience : merci ! »</li>
  </ul>
  <div class="stars stars--bottom">
    <svg viewBox="0 0 24 24"><path d="M12 1l3.4 7 7.6 1-5.5 5.3 1.3 7.6L12 18.3 5.2 21.9l1.3-7.6L1 9l7.6-1z"/></svg>
    <svg viewBox="0 0 24 24"><path d="M12 1l3.4 7 7.6 1-5.5 5.3 1.3 7.6L12 18.3 5.2 21.9l1.3-7.6L1 9l7.6-1z"/></svg>
    <svg viewBox="0 0 24 24"><path d="M12 1l3.4 7 7.6 1-5.5 5.3 1.3 7.6L12 18.3 5.2 21.9l1.3-7.6L1 9l7.6-1z"/></svg>
    <svg viewBox="0 0 24 24"><path d="M12 1l3.4 7 7.6 1-5.5 5.3 1.3 7.6L12 18.3 5.2 21.9l1.3-7.6L1 9l7.6-1z"/></svg>
    <svg viewBox="0 0 24 24"><path d="M12 1l3.4 7 7.6 1-5.5 5.3 1.3 7.6L12 18.3 5.2 21.9l1.3-7.6L1 9l7.6-1z"/></svg>
  </div>

  <div class="portrait" role="img" aria-label="Portrait photo of the mentalist in a dark suit holding a deck of cards"></div>

  <h1 class="headline">Henri Marsac lit dans vos pensées. Vraiment !</h1>
  <p class="intro"><strong>Henri Marsac</strong> est un magicien spécialisé dans la discipline du mentalisme. Il manie la télépathie, prédit l’avenir et produit des miracles avec un simple jeu de cartes ou des objets du quotidien. Sa magie est très participative et permet aux spectateurs de réaliser, eux aussi, d'incroyables prouesses magiques et mentales.</p>
  <p class="offer">Donnez une touche incroyable et fantastique à votre prochain événement : invitez un mentaliste ! Henri Marsac vous propose plusieurs formules, taillées sur mesure :</p>

  <div class="formula formula--reception">
    <svg viewBox="0 0 24 26"><path d="M12 0L23 13 12 26 1 13z"/></svg>
    <span>Réception<br>(mariage, anniversaire, …)</span>
  </div>
  <div class="formula formula--stage">
    <svg viewBox="0 0 24 26"><path d="M12 0C9 5 1 9 1 15c0 4 4 6 8 3-1 3-2 5-4 7h14c-2-2-3-4-4-7 4 3 8 1 8-3C23 9 15 5 12 0z"/></svg>
    <span>Spectacle de scène<br>(privé ou public)</span>
  </div>
  <div class="formula formula--corporate">
    <svg viewBox="0 0 24 26"><circle cx="12" cy="6" r="5.5"/><circle cx="5.5" cy="14" r="5.5"/><circle cx="18.5" cy="14" r="5.5"/><path d="M10.5 12h3c0 6 2 10 5 13H5.5c3-3 5-7 5-13z"/></svg>
    <span>Evénement d’entreprise,<br>salon, foire</span>
  </div>
  <div class="formula formula--evening">
    <svg viewBox="0 0 24 26"><path d="M12 24C5 18 0 13 0 8a6 6 0 0 1 12-2 6 6 0 0 1 12 2c0 5-5 10-12 16z"/></svg>
    <span>Soirée « mentalisme »<br>entre amis</span>
  </div>

  <p class="contact-label">Pour toute information et demande de devis :</p>
  <p class="contact">www.henrimarsac-demo.be | info@henrimarsac-demo.be | (+)32 400 12 34 56</p>
  <p class="credentials">Henri Marsac est un magicien-mentaliste professionnel, membre du Cercle International<br>des Illusionnistes et de la Ligue Mondiale des Mentalistes (USA).</p>
  <p class="disclaimer">Les témoignages sont authentiques et proviennent de clients de la saison 2016-2017</p>
</main>
</body>
</html>
```